Packaging for a new tea company

Hi guys we need a new packaging design for a tea company we are starting

Our competitors are leafara, zo ren tea

I have uploaded pictures of our competitors for you to see the sample
The label need to be catchy

Our brand is called #PlumVexaTea
We need two packaging designs one for Day Tea and one for calmora

Detox - slim - cleanse

Also needs to says 14 Day Orvalin

Target Market(s)

Young people

Industry/Entity Type

It Company

Colors
000000

Requirements
Must have
• #plumvexatea
Nice to have
• Herbal tea supplement 50gram
• Max label size 13.5cm x 16.5 cm
• Personally I like the paper brown bag as it looks like a higher quality and as the label is a sticker I think this would make the product look a lot better
Should not have
• Nothing

```html
<!DOCTYPE html>
<html lang="en">
<head>
<meta charset="utf-8">
<title>#PlumVexaTea – Detox Tea Labels</title>
<link href="https://fonts.googleapis.com/css2?family=Anton&family=Quicksand:wght@700&family=Oswald:wght@500;700&display=swap" rel="stylesheet">
<style>
  :root {
    --stage: #8a8079;
    --sky: #c3d4de;
    --plum: #8a1877;
    --plum-deep: #6f1060;
    --ink: #161616;
    --paper: #f1f1f1;
    --silver: #c8c8cc;
    --muted-dark: #9aa3a9;
    --muted-light: #d9c3d4;
  }
  * { box-sizing: border-box; margin: 0; padding: 0; }
  html, body { width: 1200px; height: 975px; overflow: hidden; }
  body {
    background: var(--stage);
    display: flex;
    align-items: center;
    justify-content: center;
    gap: 90px;
  }
  .label {
    position: relative;
    width: 420px;
    height: 432px;
    border-radius: 22px;
    padding: 50px 34px 0;
    color: var(--ink);
    --accent: var(--plum);
    --accent-text: var(--paper);
    --rule: #8f9aa1;
    --soft: var(--muted-dark);
    --leaf: rgba(255,255,255,0.45);
  }
  .label--day { background: var(--sky); }
  .label--night {
    background: var(--plum);
    color: var(--paper);
    --accent: var(--silver);
    --accent-text: var(--plum-deep);
    --rule: #c98fbd;
    --soft: var(--muted-light);
    --leaf: rgba(255,255,255,0.25);
  }
  .leaf {
    position: absolute;
    width: 56px;
    height: 22px;
    border-radius: 50%;
    background: var(--leaf);
  }
  .leaf--top { top: 16px; right: 52px; width: 70px; height: 26px; }
  .leaf--left-a { top: 146px; left: 46px; }
  .leaf--left-b { top: 226px; left: 16px; width: 40px; }
  .leaf--right { top: 306px; right: 56px; }
  .brand-tag {
    font-family: "Quicksand", sans-serif;
    font-weight: 700;
    font-size: 30px;
    text-align: center;
    letter-spacing: 0.3px;
  }
  .rule {
    height: 1px;
    background: var(--rule);
    margin: 10px -4px 0;
  }
  .title {
    font-family: "Anton", sans-serif;
    font-size: 82px;
    line-height: 1;
    letter-spacing: 1px;
    text-align: center;
    margin-top: 40px;
  }
  .title-row {
    display: flex;
    align-items: center;
    justify-content: center;
    gap: 4px;
    margin-top: 4px;
  }
  .title-row .title { margin-top: 0; }
  .badge {
    display: flex;
    align-items: center;
    background: var(--accent);
    color: var(--accent-text);
    border-radius: 12px;
    font-family: "Oswald", sans-serif;
    font-weight: 700;
  }
  .badge--days { height: 52px; padding: 0 4px 0 10px; font-size: 40px; margin-top: 10px; }
  .badge-side {
    writing-mode: vertical-rl;
    transform: rotate(180deg);
    font-family: "Oswald", sans-serif;
    font-weight: 500;
    font-size: 9px;
    letter-spacing: 0.5px;
    color: inherit;
    margin-left: 2px;
  }
  .label--day .badge-side--out { color: var(--ink); }
  .label--night .badge-side--out { color: var(--paper); }
  .footer {
    position: absolute;
    left: 22px;
    right: 20px;
    bottom: 52px;
    display: flex;
    align-items: center;
    gap: 8px;
    font-family: "Oswald", sans-serif;
    font-weight: 500;
    font-size: 13px;
    line-height: 1.15;
    text-transform: uppercase;
  }
  .claims { color: var(--soft); letter-spacing: 0.5px; }
  .footer-leaf {
    width: 20px;
    height: 44px;
    border-radius: 50%;
    background: var(--leaf);
  }
  .supplement { font-size: 15px; letter-spacing: 0.3px; }
  .supplement .hl { color: var(--plum); }
  .label--night .supplement .hl { color: var(--paper); }
  .supplement .soft { color: var(--soft); }
  .badge--weight { height: 34px; padding: 0 2px 0 6px; font-size: 26px; }
  .label--night .badge--weight { background: none; color: var(--paper); }
</style>
</head>
<body>

<section class="label label--day" aria-label="Detox tea label, light blue">
  <div class="leaf leaf--top" role="img" aria-label="Leaf ornament"></div>
  <div class="leaf leaf--left-a" role="img" aria-label="Leaf ornament"></div>
  <div class="leaf leaf--left-b" role="img" aria-label="Leaf ornament"></div>
  <div class="leaf leaf--right" role="img" aria-label="Leaf ornament"></div>
  <p class="brand-tag">#PlumVexaTea</p>
  <div class="rule"></div>
  <h1 class="title">DETOX</h1>
  <div class="title-row">
    <div class="badge badge--days">14</div>
    <span class="badge-side badge-side--out">DAY ORVALIN</span>
    <h2 class="title">TEA</h2>
  </div>
  <div class="footer">
    <p class="claims">Full of antioxidants<br>and immune booster</p>
    <div class="footer-leaf" role="img" aria-label="Leaf ornament"></div>
    <p class="supplement"><span class="hl">Herbal</span> <span class="soft">tea</span><br>Supplement</p>
    <div class="badge badge--weight">50<span class="badge-side">GRAM</span></div>
  </div>
</section>

<section class="label label--night" aria-label="Detox tea label, plum">
  <div class="leaf leaf--top" role="img" aria-label="Leaf ornament"></div>
  <div class="leaf leaf--left-a" role="img" aria-label="Leaf ornament"></div>
  <div class="leaf leaf--left-b" role="img" aria-label="Leaf ornament"></div>
  <div class="leaf leaf--right" role="img" aria-label="Leaf ornament"></div>
  <p class="brand-tag">#PlumVexaTea</p>
  <div class="rule"></div>
  <h1 class="title">DETOX</h1>
  <div class="title-row">
    <div class="badge badge--days">14</div>
    <span class="badge-side badge-side--out">DAY ORVALIN</span>
    <h2 class="title">TEA</h2>
  </div>
  <div class="footer">
    <p class="claims">Full of antioxidants<br>and immune booster</p>
    <div class="footer-leaf" role="img" aria-label="Leaf ornament"></div>
    <p class="supplement"><span class="hl">Herbal</span> <span class="soft">tea</span><br>Supplement</p>
    <div class="badge badge--weight">50<span class="badge-side">GRAM</span></div>
  </div>
</section>

</body>
</html>
```